PELDRAX Business Cards

We require a business card for our company that provides IT consulting services. We already have a logo that needs to be used on the card. We want a clean professional looking design that incorporates our colours. Our main focus is providing managed services to business, which involves us looking after all of their IT requirements including managing servers/networks, projects, and procurement.

Industry/Entity Type

Information Technology

Requirements
Must have
• our logo, contact information, name, title, phone numbers

```html
<!DOCTYPE html>
<html lang="en">
<head>
<meta charset="utf-8">
<title>PELDRAX Business Cards</title>
<link href="https://fonts.googleapis.com/css2?family=Montserrat:wght@600&family=Roboto:wght@400;700&display=swap" rel="stylesheet">
<style>
  :root {
    --brand-blue: #1893cf;
    --brand-blue-soft: #3fa3d8;
    --card-white: #ffffff;
    --backdrop: #2b2b2d;
  }
  html, body {
    margin: 0;
    padding: 0;
    width: 1200px;
    height: 880px;
    overflow: hidden;
    background: var(--backdrop);
  }
  .canvas {
    position: relative;
    width: 1200px;
    height: 880px;
  }
  .card {
    position: absolute;
    width: 560px;
    height: 320px;
    border-radius: 22px;
    overflow: hidden;
    box-shadow: 0 14px 30px rgba(0,0,0,0.45);
  }
  .card-front {
    left: 60px;
    top: 80px;
    background: var(--brand-blue);
    display: flex;
    align-items: center;
    justify-content: center;
  }
  .wordmark {
    display: flex;
    align-items: center;
    gap: 14px;
    font-family: "Montserrat", sans-serif;
    font-weight: 600;
    letter-spacing: 3px;
  }
  .wordmark-dot {
    width: 30px;
    height: 30px;
    border-radius: 50%;
  }
  .card-front .wordmark { color: var(--card-white); font-size: 54px; }
  .card-front .wordmark-dot { background: var(--card-white); }

  .card-back {
    left: 580px;
    top: 480px;
    background: var(--card-white);
  }
  .card-back .wordmark {
    position: absolute;
    left: 0;
    right: 0;
    top: 46px;
    justify-content: center;
    color: var(--brand-blue);
    font-size: 50px;
  }
  .card-back .wordmark-dot { background: var(--brand-blue); }
  .info-band {
    position: absolute;
    left: 0;
    right: 0;
    top: 168px;
    height: 100px;
    background: var(--brand-blue);
  }
  .person {
    position: absolute;
    left: 150px;
    top: 120px;
    text-align: right;
    font-family: "Roboto", sans-serif;
    color: var(--brand-blue);
  }
  .person-name {
    font-weight: 700;
    font-size: 20px;
    margin: 0;
  }
  .person-title {
    font-size: 15px;
    margin: 2px 0 0;
  }
  .divider {
    position: absolute;
    left: 290px;
    top: 112px;
    width: 2px;
    height: 48px;
    background: var(--brand-blue);
  }
  .contacts {
    position: absolute;
    left: 306px;
    top: 110px;
    margin: 0;
    padding: 0;
    list-style: none;
    font-family: "Roboto", sans-serif;
    font-size: 14px;
    color: var(--brand-blue);
  }
  .contacts li {
    display: flex;
    align-items: center;
    gap: 7px;
    height: 18px;
  }
  .contacts svg { width: 14px; height: 14px; }
  .address {
    position: absolute;
    left: 0;
    right: 0;
    top: 182px;
    text-align: center;
    font-family: "Roboto", sans-serif;
    font-size: 15px;
    color: var(--card-white);
    margin: 0;
  }
  .band-name {
    position: absolute;
    left: 0;
    right: 0;
    top: 220px;
    text-align: center;
    font-family: "Roboto", sans-serif;
    color: var(--card-white);
  }
  .footer-strip {
    position: absolute;
    left: 0;
    right: 0;
    top: 268px;
    bottom: 0;
    display: flex;
    align-items: center;
    justify-content: center;
    font-family: "Roboto", sans-serif;
    font-size: 15px;
    color: var(--brand-blue);
  }
</style>
</head>
<body>
<main class="canvas">
  <section class="card card-front" aria-label="Card front">
    <div class="wordmark"><span class="wordmark-dot"></span>PELDRAX</div>
  </section>

  <section class="card card-back" aria-label="Card back">
    <div class="wordmark"><span class="wordmark-dot"></span>PELDRAX</div>

    <ul class="contacts">
      <li>
        <svg viewBox="0 0 16 16" aria-hidden="true"><circle cx="8" cy="8" r="7" fill="none" stroke="currentColor" stroke-width="1.4"/><path d="M5 4.5c0 4 2.5 6.5 6.5 6.5l.5-1.6-1.8-.8-.9.9c-1.2-.5-2-1.3-2.5-2.5l.9-.9-.8-1.8z" fill="currentColor"/></svg>
        +01 4821 7730
      </li>
      <li>
        <svg viewBox="0 0 16 16" aria-hidden="true"><circle cx="8" cy="8" r="7" fill="none" stroke="currentColor" stroke-width="1.4"/><rect x="4" y="5.5" width="8" height="5" fill="none" stroke="currentColor" stroke-width="1.1"/><path d="M4 5.5l4 3 4-3" fill="none" stroke="currentColor" stroke-width="1.1"/></svg>
        info@peldraxmail.com
      </li>
      <li>
        <svg viewBox="0 0 16 16" aria-hidden="true"><circle cx="8" cy="8" r="7" fill="none" stroke="currentColor" stroke-width="1.4"/><circle cx="8" cy="8" r="4" fill="none" stroke="currentColor" stroke-width="1"/><path d="M4 8h8M8 4v8" stroke="currentColor" stroke-width="1"/></svg>
        www.peldraxweb.com
      </li>
    </ul>
    <div class="divider"></div>
    <div class="person">
      <p class="person-name">Mara Holt</p>
      <p class="person-title">President &amp; CEO</p>
    </div>

    <div class="info-band"></div>
    <div class="footer-strip">PO BOX 481, Hollis Road, 4th Lane, Leeds</div>
  </section>
</main>
</body>
</html>
```